Creative, Modern and Conversion based Web Design

Kolvex Digital has recently launched a new logo and as part of our companies rebranding, we need a new website aimed towards the UK B2B marketplace.

The website needs to deliver a modern and creative website design whilst ensuring the design is tailored towards conversion optimisation.

This site must drive point of contact either from an online form, via a direct telephone call or Skype connection.

Our sales are all offline so the website will be a simple, elegant and stunning information portal.

Kolvex Digital offers Digital Marketing services to companies throughout the UK - our target audiences are companies that turnover a minimum of 3 million pounds a year and as such we need to deliver a professional image that installs confidence in our companies abilities.

We do not like websites that are reliant upon stock photography - we are happy for stock photography to be used in a small way however the site must not look like a template filled with stock photography.

What do we do

We supply digital marketing services to those companies who demand a strong return on investment - our company prides itself on delivering successful campaigns that help establish long-term profitable relationships.

A lot of the information presented on our old site is relevant today however the design sucks. So please use the information on our current website as a foundation for your design content.

I am looking for several page designs including

"Home Page" Desktop Version
"Service Page" Desktop Version
"Blog Page" Desktop Version

"Home Page" Mobile Version
"Service Page" Mobile Version
"Blog Page" Mobile Version

In the 1st instance please only submit a single design for the "Home Page" Desktop Version - those designers that we are impressed with will be asked to complete the other designs before a winner is selected.

I like modern clean fonts - the site needs to welcome the reader and encourage them to absorb the information - not to overload and make them leave.

The site must be designed to naturally fit our companies new logo.

NO TEMPLATES

Target Market(s)

B2b - 3 million turnover and above

Industry/Entity Type

Digital Marketing

Number of Pages Required

3 page

Requirements
Must have
• Blended well with the companies logo
• We need conversion optimisation to be a huge part of the design - we considered a conversation when a potential customer reaches out to use via - web form, telephone or skype
• The current content on the old website fits today's business but the design sucks.
• www.kolvexdigital-example.com
Nice to have
• We need 3 pages (in 2 variants Desktop and Mobile)
• Home Page
• Service Page
• Blog Page
• Please only deliver the "Home Page" desktop version - if we are happy with your design we will aks for the additional pages
Should not have
• No templates and not stock photo heavy design

```html
<!DOCTYPE html>
<html lang="en">
<head>
<meta charset="utf-8">
<title>Digital Marketing Services</title>
<link rel="stylesheet" href="https://fonts.googleapis.com/css2?family=Manrope:wght@400;500&display=swap">
<style>
  :root {
    --backdrop: #eef4fb;
    --page: #ffffff;
    --brand-blue: #1a0df2;
    --ink: #0a0a0a;
    --muted: #5f6670;
    --nav-ink: #5a5f66;
    --soft-lilac: #f7f6fd;
    --curve: #e6e3f7;
    --art-deep: #2a14e6;
    --art-mid: #2f8ff5;
    --art-light: #4ff2dc;
  }
  * { box-sizing: border-box; margin: 0; padding: 0; }
  html, body {
    width: 1200px; height: 1200px; overflow: hidden;
    background: var(--backdrop);
    font-family: "Manrope", sans-serif;
  }
  .landing {
    position: absolute; left: 0; top: 248px;
    width: 1200px; height: 674px;
    background: var(--page);
    overflow: hidden;
  }
  .landing__backdrop { position: absolute; inset: 0; }
  .brand {
    position: absolute; left: 121px; top: 12px;
    font-size: 20px; font-weight: 400; color: var(--brand-blue);
    word-spacing: 10px;
  }
  .main-nav {
    position: absolute; top: 23px; left: 588px;
    display: flex; gap: 40px;
    font-size: 14px; line-height: 20px; color: var(--nav-ink);
  }
  .main-nav a { color: inherit; text-decoration: none; }
  .btn-get-started {
    position: absolute; left: 970px; top: 13px;
    width: 109px; height: 41px;
    background: var(--brand-blue); color: #fff;
    border-radius: 2px;
    font-size: 14px; display: flex; align-items: center; justify-content: center;
    text-decoration: none;
  }
  .hero-title {
    position: absolute; left: 21px; top: 222px;
    font-size: 63px; font-weight: 400; line-height: 64px;
    color: var(--ink); letter-spacing: -0.5px;
  }
  .hero-intro {
    position: absolute; left: 121px; top: 408px; width: 300px;
    font-size: 14px; line-height: 18px; color: var(--muted);
  }
  .btn-learn-more {
    position: absolute; left: 121px; top: 550px;
    width: 145px; height: 54px; border-radius: 27px;
    background: var(--brand-blue); color: #fff;
    font-size: 18px; display: flex; align-items: center; justify-content: center;
    text-decoration: none;
  }
  .link-contact {
    position: absolute; left: 285px; top: 568px;
    font-size: 14px; color: var(--brand-blue); text-decoration: underline;
  }
  .hero-art {
    position: absolute; left: 600px; top: 70px;
    width: 590px; height: 600px;
  }
</style>
</head>
<body>
  <main class="landing">
    <svg class="landing__backdrop" width="1200" height="674" viewBox="0 0 1200 674" aria-hidden="true">
      <path d="M480 0 C 420 140, 440 250, 560 330 C 700 420, 720 540, 590 674 L 1200 674 L 1200 0 Z" fill="var(--soft-lilac)" opacity="0.6"/>
      <path d="M480 0 C 420 140, 440 250, 560 330 C 700 420, 720 540, 590 674" fill="none" stroke="var(--curve)" stroke-width="2"/>
    </svg>

    <div class="brand">company logo</div>

    <nav class="main-nav">
      <a href="#">Home</a>
      <a href="#">About Us</a>
      <a href="#">Services</a>
      <a href="#contact">Contact Us</a>
    </nav>
    <a class="btn-get-started" href="#contact">Get Started</a>

    <h1 class="hero-title">Digital Marketing<br>Services</h1>
    <p class="hero-intro">Small intro or information about the services provided online!</p>

    <a class="btn-learn-more" href="#">Learn more</a>
    <a class="link-contact" href="#contact">or contact</a>

    <svg class="hero-art" viewBox="0 0 590 600" role="img" aria-label="Illustration of a person stepping out of a tablet surrounded by social media icons: likes, messages, notifications, photos, video and email">
      <defs>
        <linearGradient id="artFill" x1="0.2" y1="0" x2="0.8" y2="1">
          <stop offset="0" stop-color="var(--art-deep)"/>
          <stop offset="0.55" stop-color="var(--art-mid)"/>
          <stop offset="1" stop-color="var(--art-light)"/>
        </linearGradient>
      </defs>
      <path d="M150 70 C 260 -10, 470 20, 560 110 C 600 160, 590 470, 520 560 C 430 640, 200 600, 120 520 C 40 440, 10 300, 60 190 C 80 140, 110 100, 150 70 Z" fill="var(--soft-lilac)"/>
      <path d="M300 80 C 420 60, 560 140, 575 270 C 590 410, 520 520, 440 540 C 360 560, 320 470, 300 400 C 270 300, 220 250, 250 150 C 260 115, 275 88, 300 80 Z" fill="url(#artFill)"/>
    </svg>
  </main>
</body>
</html>
```